Torvane Travel Business Card Design

We need a new business card design for our travel agency business - Torvane Travel. We design packages to some of the most popular travel destinations in the world for groups, individuals and also tailor-make personalised packages. Our logo attached must be used. On the back of the card we would like a list of all websites under our Torvane brand to be posted. We would like clean, modern, simple design.

Industry/Entity Type

Travel Agent

Contact Information for Business Card

Owen Pridmore
National Sales Manager
Reservations: 1300 742 689
Tel: 61 28473 5096
Fax: 61 2847 3971
Email: owen@torvanetravel.com.au
Web: www.torvanetravel.com.au

Address: Level 1, 417 Harwick Street
Sydney NSW 2000 Australia

Requirements
Must have
• On the back of the card we want all websites listed under our Torvane brand.
• Torvane Travel Group - Wholesale Specialists
• www.qpjourneys.com.au - New Caledonia
• www.bravelmijourneys.com.au - Tahiti
• www.sorvenbreakhub.com.au - China
Nice to have
• Modern, clean lined, simple and fresh
Should not have
• Look dull

```html
<!DOCTYPE html>
<html lang="en">
<head>
<meta charset="utf-8">
<title>Torvane Travel – Business Card</title>
<link rel="stylesheet" href="https://fonts.googleapis.com/css2?family=Source+Sans+3:wght@400;600&display=swap">
<style>
  :root {
    --backdrop: #2b2b2b;
    --card-white: #f7f7f7;
    --navy: #2a2a7c;
    --red: #e41b23;
    --white: #ffffff;
  }
  * { margin: 0; padding: 0; box-sizing: border-box; }
  html, body {
    width: 1200px; height: 750px; overflow: hidden;
    background: var(--backdrop);
    font-family: "Source Sans 3", sans-serif;
  }
  .stage { position: relative; width: 1200px; height: 750px; }
  .card {
    position: absolute; top: 228px; width: 461px; height: 262px; overflow: hidden;
  }
  .card-front { left: 124px; background: var(--card-white); }
  .card-back { left: 618px; background: var(--red); }

  .swoosh { position: absolute; inset: 0; width: 461px; height: 262px; }

  .brand {
    position: absolute; left: 34px; top: 44px;
    display: flex; align-items: center; gap: 8px;
  }
  .brand-dot { width: 12px; height: 12px; border-radius: 50%; background: var(--red); }
  .brand-name {
    font-size: 33px; font-weight: 600; color: var(--navy); letter-spacing: -0.5px; line-height: 1;
  }

  .person { position: absolute; left: 34px; top: 105px; }
  .person-name { font-size: 17px; font-weight: 600; color: var(--navy); line-height: 1.2; }
  .person-title { font-size: 12.5px; color: var(--red); line-height: 1.3; }

  .contact-list {
    position: absolute; right: 18px; top: 140px; list-style: none;
  }
  .contact-item {
    display: flex; justify-content: flex-end; align-items: center; gap: 9px;
    height: 17.6px; font-size: 11.5px; color: var(--white);
  }
  .contact-icon { width: 11px; height: 11px; fill: var(--red); flex: none; }

  .address {
    position: absolute; right: 18px; top: 232px;
    font-size: 11.5px; color: var(--white);
  }

  .wholesale {
    position: absolute; left: 0; right: 0; top: 101px; text-align: center; color: var(--white);
  }
  .wholesale-title { font-size: 13.5px; font-weight: 600; line-height: 1.35; }
  .wholesale-site { font-size: 11.5px; line-height: 1.4; }
</style>
</head>
<body>
<div class="stage">

  <section class="card card-front">
    <svg class="swoosh" viewBox="0 0 461 262" aria-hidden="true">
      <path d="M0,262 C55,205 150,190 260,162 C360,137 440,92 461,14 L461,262 Z" fill="var(--navy)"/>
      <path d="M400,112 C435,90 455,60 461,22 L461,10 C452,55 430,88 398,110 Z" fill="var(--navy)"/>
      <path d="M0,262 L0,248 C40,212 100,195 170,186 C100,200 40,225 6,262 Z" fill="var(--red)"/>
    </svg>

    <div class="brand">
      <span class="brand-name">Torvane Travel</span>
      <span class="brand-dot"></span>
    </div>

    <div class="person">
      <p class="person-name">Owen Pridmore</p>
      <p class="person-title">National Sales Manager</p>
    </div>

    <ul class="contact-list">
      <li class="contact-item">61 28473 5096
        <svg class="contact-icon" viewBox="0 0 12 12"><path d="M2.5 0.5 L4.5 0.5 L5.2 3.2 L3.8 4.3 C4.5 6 6 7.5 7.7 8.2 L8.8 6.8 L11.5 7.5 L11.5 9.5 C11.5 10.8 10.5 11.5 9.5 11.5 C4.5 11 1 7.5 0.5 2.5 C0.5 1.4 1.3 0.5 2.5 0.5 Z"/></svg>
      </li>
      <li class="contact-item">61 28473 5096
        <svg class="contact-icon" viewBox="0 0 12 12"><rect x="3" y="0.5" width="6" height="3"/><rect x="0.5" y="4.5" width="11" height="5" rx="1"/><rect x="3" y="8.5" width="6" height="3"/></svg>
      </li>
      <li class="contact-item">1300 742 689 (Reservations)
        <svg class="contact-icon" viewBox="0 0 12 12"><path d="M2.5 0.5 L4.5 0.5 L5.2 3.2 L3.8 4.3 C4.5 6 6 7.5 7.7 8.2 L8.8 6.8 L11.5 7.5 L11.5 9.5 C11.5 10.8 10.5 11.5 9.5 11.5 C4.5 11 1 7.5 0.5 2.5 C0.5 1.4 1.3 0.5 2.5 0.5 Z"/></svg>
      </li>
      <li class="contact-item">owen@torvanetravel.com.au
        <svg class="contact-icon" viewBox="0 0 12 12"><rect x="0.5" y="2" width="11" height="8"/><path d="M0.5 2 L6 6.5 L11.5 2" fill="none" stroke="var(--navy)" stroke-width="1"/></svg>
      </li>
      <li class="contact-item">www.torvanetravel.com.au
        <svg class="contact-icon" viewBox="0 0 12 12"><circle cx="6" cy="6" r="5.5"/><path d="M0.5 6 H11.5 M6 0.5 C3.5 3 3.5 9 6 11.5 M6 0.5 C8.5 3 8.5 9 6 11.5" fill="none" stroke="var(--navy)" stroke-width="0.8"/></svg>
      </li>
    </ul>

    <p class="address">Level 1, 417 Harwick Street, Sydney NSW 2000 Australia</p>
  </section>

  <section class="card card-back">
    <div class="wholesale">
      <p class="wholesale-title">Torvane Travel Group - Wholesale Specialists</p>
      <p class="wholesale-site">www.qpjourneys.com.au - New Caledonia</p>
      <p class="wholesale-site">www.bravelmijourneys.com.au - Tahiti</p>
      <p class="wholesale-site">www.sorvenbreakhub.com.au - China</p>
    </div>
  </section>

</div>
</body>
</html>
```